Law Office needs stationery design and business card

I currently have been using the same letterhead for the last 8 years. Since i 'm about to adding another location, I want to revamp my letterhead and business card. I already have a logo i'm happy with. I will upload my current letterhead, fax sheet, envelope, and logos. I need a business card also. I have 2 locations, 1 phone number, 1 fax line, website, etc. If possible and fitting with the design, I would like to keep the same information listed currently on the letterhead.

**Keep in mind, I also NEED A FAX SHEET COVER. thank you

Hello, Please submit a Gray Scale or Black and White version of your designs also, since most of the time I will be printing NON color stationery. I will seldom use a color print for my letterhead, I would like to have a color version for my benefit, however i will print in grayscale majority of the time . For the Business Card, that can just be in color. When I get my business cards they will be in color.Thank youEnrique Added Sunday, September 18, 2016

```html
<!DOCTYPE html>
<html lang="en">
<head>
<meta charset="utf-8">
<title>Hartwell Law – Business Card</title>
<link rel="stylesheet" href="https://fonts.googleapis.com/css2?family=Source+Sans+3:wght@400;600&display=swap">
<style>
  :root {
    --page-bg: #e9e7e3;
    --card-dark: #1f1d1d;
    --card-dark-edge: #2c2a2a;
    --card-light: #ffffff;
    --text-light: #e8e8e8;
    --text-muted: #8e8e8e;
    --mark-grey: #7d7d7d;
    --ink: #151515;
    --rule: #9a9a9a;
  }
  * { box-sizing: border-box; margin: 0; padding: 0; }
  html, body { width: 1200px; height: 950px; overflow: hidden; }
  body {
    background: var(--page-bg);
    font-family: "Source Sans 3", "Helvetica Neue", Arial, sans-serif;
    position: relative;
  }
  .card {
    position: absolute;
    left: 250px;
    width: 700px;
    height: 400px;
    box-shadow: 0 6px 18px rgba(0,0,0,0.18);
  }
  .card--front {
    top: 50px;
    background: linear-gradient(135deg, var(--card-dark-edge) 0%, var(--card-dark) 60%);
    color: var(--text-light);
  }
  .card--back {
    top: 500px;
    background: var(--card-light);
  }

  /* Front: identity block */
  .identity-mark {
    position: absolute;
    left: 150px;
    top: 70px;
    width: 170px;
    text-align: center;
  }
  .identity-mark__square {
    display: block;
    width: 44px;
    height: 44px;
    margin: 0 auto 10px;
    background: var(--mark-grey);
  }
  .identity-mark__name {
    font-size: 15px;
    font-weight: 600;
    letter-spacing: 3px;
    color: var(--text-light);
  }
  .attorney-name {
    position: absolute;
    left: 60px;
    top: 160px;
    width: 300px;
    text-align: right;
    font-size: 26px;
    font-weight: 400;
    color: var(--text-muted);
  }
  .attorney-rule {
    position: absolute;
    left: 30px;
    top: 200px;
    width: 330px;
    height: 1px;
    background: var(--rule);
  }
  .attorney-title {
    position: absolute;
    left: 60px;
    top: 204px;
    width: 300px;
    text-align: right;
    font-size: 16px;
    color: var(--text-light);
  }

  /* Front: offices */
  .offices {
    position: absolute;
    left: 30px;
    top: 270px;
    font-size: 17px;
    line-height: 24px;
    color: var(--text-light);
  }
  .offices__rule {
    position: absolute;
    left: 30px;
    top: 262px;
    width: 260px;
    height: 1px;
    background: var(--rule);
  }

  /* Front: contact list */
  .contact-rule {
    position: absolute;
    right: 30px;
    top: 40px;
    width: 240px;
    height: 1px;
    background: var(--rule);
  }
  .contact {
    position: absolute;
    right: 30px;
    top: 52px;
    list-style: none;
    font-size: 16px;
    line-height: 26px;
    text-align: right;
    color: var(--text-light);
  }
  .contact__item {
    display: flex;
    justify-content: flex-end;
    align-items: center;
    gap: 10px;
  }
  .contact__icon {
    width: 14px;
    height: 14px;
    flex: none;
  }

  /* Back */
  .brand {
    position: absolute;
    left: 0;
    top: 0;
    width: 700px;
    height: 400px;
    display: flex;
    align-items: center;
    justify-content: center;
    gap: 22px;
  }
  .brand__square {
    width: 60px;
    height: 60px;
    background: var(--ink);
  }
  .brand__name {
    font-size: 52px;
    font-weight: 600;
    letter-spacing: 4px;
    color: var(--ink);
  }
</style>
</head>
<body>

<section class="card card--front">
  <div class="identity-mark">
    <span class="identity-mark__square"></span>
    <span class="identity-mark__name">HARTWELL LAW</span>
  </div>

  <h1 class="attorney-name">Gustavo Hartwell Esq.</h1>
  <div class="attorney-rule"></div>
  <p class="attorney-title">Attorney</p>

  <div class="offices__rule"></div>
  <address class="offices">
    418 Harlow Ave.<br>
    Suite 200, Brookdale, PA 19002<br>
    726 Linden St.<br>
    Carverton, PA 19010
  </address>

  <div class="contact-rule"></div>
  <ul class="contact">
    <li class="contact__item">610.555.0142
      <svg class="contact__icon" viewBox="0 0 16 16" fill="#e8e8e8" aria-hidden="true"><path d="M3.5 1.5l2.5 0 1 3.5-1.8 1.2c.8 1.7 2 2.9 3.6 3.6L10 8l3.5 1v2.5c0 1-1 2-2 2C6 13.5 2.5 10 2.5 4.5c0-1 .5-3 1-3z"/></svg>
    </li>
    <li class="contact__item">484.555.0187
      <svg class="contact__icon" viewBox="0 0 16 16" aria-hidden="true"><rect x="4" y="1" width="8" height="14" rx="1.5" fill="none" stroke="#e8e8e8" stroke-width="1.4"/><circle cx="8" cy="12.5" r="0.9" fill="#e8e8e8"/></svg>
    </li>
    <li class="contact__item">Gustavo@HartwellLaw.com
      <svg class="contact__icon" viewBox="0 0 16 16" aria-hidden="true"><rect x="1" y="3" width="14" height="10" rx="1" fill="#e8e8e8"/><path d="M1.5 3.8L8 9l6.5-5.2" fill="none" stroke="#1f1d1d" stroke-width="1.3"/></svg>
    </li>
    <li class="contact__item">www.HartwellLaw.com
      <svg class="contact__icon" viewBox="0 0 16 16" aria-hidden="true"><circle cx="8" cy="8" r="6.5" fill="#e8e8e8"/><path d="M1.5 8h13M8 1.5c-2.5 3-2.5 10 0 13M8 1.5c2.5 3 2.5 10 0 13" fill="none" stroke="#1f1d1d" stroke-width="1"/></svg>
    </li>
  </ul>
</section>

<section class="card card--back">
  <div class="brand">
    <span class="brand__square"></span>
    <span class="brand__name">HARTWELL LAW</span>
  </div>
</section>

</body>
</html>
```